Designing the score views for a social gaming app

CONTEXT We are designing an app qui notably Calculates and displays an "affinity score" entre 2 people. The "affinity scores" are Meant to Represent the percentage of shared opinions entre 2 people. The affinity score can be global (encompassing all topics) or by topic. Typical topics Would Be: cinema, music, politics, food ... The affinity score Range is 0-100. 0 means clustering que le 2 people do not share Any opinions / tastes. 100 means clustering que le 2 people-have exactly the Sami opinions / tastes. The app targets people entre 16 and 25 yo. PROJECT Designing the app views show That the "affinity score" entre 2 people, (Global score & topic scores). The overall score view must contain: - the first name of the 2 people - Their profile pictures, in circle or square size - an overall score Represented with numbers - a symbolization of the percentage (Either the "%" symbol gold circular progress bar or any good idea) - the TOP score (The Highest score Among the topic scores) - the FLOP score (the lowest score Among the topic scores) - a list of topic scores - a topic can be illustrated by an icon or not - has topic score can be a number, a progress or bar any good idea - Each topic is a clickable cell That redirects to a topic score view The topic score view must contain: - a summary of the 2 people info (profile picture first name) - the topic name (and Eventually the topic icon) - the topic score - the total number of issues taken into account to calculate the score - a button to refine the score REQUIREMENTS For Quorvel 4 to 6 (autolayout) Main are used: AvenirNext Main foreground colors: Black (RGB: 000000) Red (RGB: FF4400) Grey (RGB: 666666) Flat and pure design The design must be friendly and target people entre 16 and 25 yo. It must look like a game. SAMPLES See attached: two drafts of design
People entre 16 and 25 yo and Having an Quorvel
Dating

```html
<!DOCTYPE html>
<html lang="en">
<head>
<meta charset="utf-8">
<title>Affinity Score Views</title>
<link href="https://fonts.googleapis.com/css2?family=Nunito+Sans:wght@300;400;600;700&display=swap" rel="stylesheet">
<style>
:root{
  --canvas:#e2e2e2;
  --screen:#ebebeb;
  --bar:#ffffff;
  --ink:#000000;
  --grey:#666666;
  --grey-dark:#555555;
  --red:#ff4400;
  --white:#ffffff;
}
*{box-sizing:border-box;margin:0;padding:0}
html,body{width:1200px;height:1193px;overflow:hidden;background:var(--canvas)}
body{font-family:"Nunito Sans",sans-serif;color:var(--ink)}
.stage{position:absolute;left:0;top:0;width:1424px;height:1416px;transform:scale(0.8427);transform-origin:0 0}
.screen{position:absolute;width:412px;height:726px;background:var(--screen);overflow:hidden;border:3px solid #333}
.screen--overview{left:178px;top:352px}
.screen--topic{left:784px;top:350px}
.abs{position:absolute}
.statusbar{left:0;top:0;width:100%;height:30px;background:var(--bar);font-size:13px;font-weight:600}
.statusbar .carrier{left:14px;top:6px;display:flex;align-items:center;gap:4px}
.dots{display:flex;gap:2px}
.dots i{width:7px;height:7px;border-radius:50%;border:1px solid var(--ink)}
.dots i.on{background:var(--ink)}
.statusbar .time{left:0;width:100%;top:7px;text-align:center}
.battery{right:16px;top:9px;width:28px;height:11px;border-radius:4px;background:var(--ink)}
.navbar{left:0;top:30px;width:100%;height:58px;background:var(--bar)}
.navbar .title{width:100%;top:12px;text-align:center;font-size:24px;font-weight:600}
.navbar .back{left:24px;top:16px}
.navbar .share{right:22px;top:8px}
.avatar{border-radius:50%;border:7px solid var(--grey)}
.avatar--you{left:12px;top:118px;width:120px;height:120px;background:radial-gradient(circle at 50% 45%,#d9a88a 0 35%,#8a5a3c 60%,#3a3a3a 100%)}
.avatar--carla{left:284px;top:120px;width:118px;height:118px;background:radial-gradient(circle at 50% 50%,#c99581 0 22%,#2a2225 45%,#3d4a58 100%)}
.connector{height:4px;background:var(--grey)}
.pill{background:var(--grey);color:var(--white);border-radius:30px;display:flex;align-items:center;justify-content:center;font-size:24px}
.name--you{left:165px;top:126px;width:78px;height:31px}
.name--carla{left:153px;top:187px;width:104px;height:31px}
.ring{left:0;top:260px}
.big-score{left:24px;top:330px;width:180px;text-align:center;font-size:76px;font-weight:300;color:var(--grey-dark);line-height:1}
.new-top{left:24px;top:408px;width:180px;text-align:center;font-size:13px;color:var(--grey-dark)}
.verdict{left:220px;top:280px;width:184px;text-align:center;font-size:30px;line-height:29px}
.verdict .hot{display:block;color:var(--red);font-size:40px;line-height:44px;margin-top:4px}
.stat{height:36px;border-radius:18px;background:var(--grey);color:var(--white);display:flex;align-items:center;justify-content:center;gap:6px}
.stat small{font-size:9px;line-height:9px;text-align:center}
.stat b{font-weight:400;font-size:24px}
.stat--top{left:232px;top:418px;width:82px}
.stat--flop{left:319px;top:418px;width:82px}
.topic{height:52px;background:var(--grey);color:var(--white);font-size:23px;display:flex;align-items:center}
.topic--left{left:0;width:174px;border-radius:0 26px 26px 0;padding-left:12px;gap:14px}
.topic--right{left:234px;width:178px;border-radius:26px 0 0 26px;padding-left:14px;gap:22px}
.chev{color:var(--red);font-size:20px}
.topic--left .chev{margin-left:auto;margin-right:10px}
.play{left:110px;top:674px;width:189px;height:40px;font-size:22px}
.band{left:0;top:291px;width:244px;height:73px;background:var(--grey);border-radius:0 37px 37px 0;color:var(--white);display:flex;align-items:center;gap:22px;padding-left:16px;font-size:32px}
.mini-label{font-size:11px;color:var(--grey-dark);top:286px}
.mini-num{font-size:20px;color:var(--grey-dark);top:322px}
.panel{left:0;top:383px;width:386px;height:204px;background:var(--grey);border-radius:0 102px 102px 0;color:var(--white)}
.panel .row{left:0;width:342px;text-align:center}
.panel .lbl{font-size:22px}
.panel .val{font-size:46px;font-weight:300;line-height:1}
.panel .rule{left:92px;top:99px;width:151px;height:1px;background:#9a9a9a}
.action{height:55px;top:620px;font-size:22px;background:var(--grey);color:var(--white);display:flex;align-items:center}
.action--reset{left:0;width:178px;border-radius:0 28px 28px 0;padding-left:26px}
.action--next{left:213px;width:200px;border-radius:28px 0 0 28px;padding-left:14px;gap:4px}
</style>
</head>
<body>
<div class="stage">

<!-- Overall score view -->
<section class="screen screen--overview">
  <div class="abs statusbar">
    <div class="abs carrier"><span class="dots"><i class="on"></i><i class="on"></i><i></i><i></i><i></i></span>Norvia</div>
    <div class="abs time">9:32PM</div>
    <div class="abs battery"></div>
  </div>
  <div class="abs navbar">
    <svg class="abs back" width="12" height="20" viewBox="0 0 12 20"><path d="M10 2 2 10l8 8" fill="none" stroke="#ff4400" stroke-width="2"/></svg>
    <div class="abs title">You &amp; Carla</div>
    <svg class="abs share" width="24" height="34" viewBox="0 0 24 34"><path d="M8 10H1v23h22V10h-7M12 1v20M7 6l5-5 5 5" fill="none" stroke="#ff4400" stroke-width="2"/></svg>
  </div>

  <div class="abs connector" style="left:120px;top:139px;width:50px"></div>
  <div class="abs connector" style="left:250px;top:201px;width:40px"></div>
  <div class="abs avatar avatar--you" role="img" aria-label="Profile photo of You"></div>
  <div class="abs avatar avatar--carla" role="img" aria-label="Profile photo of Carla"></div>
  <div class="abs pill name--you">You</div>
  <div class="abs pill name--carla">Carla</div>

  <svg class="abs ring" width="230" height="230" viewBox="0 260 230 230"><path d="M114 284A92 92 0 1 0 184.5 435" fill="none" stroke="#ff4400" stroke-width="22"/></svg>
  <div class="abs big-score">58</div>
  <div class="abs new-top">NEW TOP SCORE!</div>

  <div class="abs verdict">Your<br>Score<br>is<span class="hot">Not Bad.</span></div>
  <div class="abs stat stat--top"><small>TOP<br>SCORE</small><b>58</b></div>
  <div class="abs stat stat--flop"><small>FLOP<br>SCORE</small><b>0</b></div>

  <div class="abs topic topic--left" style="top:536px">
    <svg width="28" height="20" viewBox="0 0 28 20"><path d="M3 3h16l6 2v10l-6 2H3a2 2 0 0 1-2-2V5a2 2 0 0 1 2-2z" fill="#fff"/><circle cx="24" cy="8" r="1.5" fill="#666"/><circle cx="24" cy="12" r="1.5" fill="#666"/></svg>
    Cinema<span class="chev">›</span>
  </div>
  <div class="abs topic topic--right" style="top:536px">
    <span class="chev">‹</span>Food
    <svg width="26" height="26" viewBox="0 0 26 26"><circle cx="13" cy="13" r="12" fill="#fff"/><path d="M13 13V3a10 10 0 0 1 10 10z" fill="#999"/></svg>
  </div>
  <div class="abs topic topic--left" style="top:605px">
    <svg width="26" height="28" viewBox="0 0 26 28"><path d="M13 2l2 5h-4zM6 10a7 5 0 0 1 14 0zM4 11h18v2H4zM5 14h2v9H5zm5 0h2v9h-2zm4 0h2v9h-2zm5 0h2v9h-2zM2 24h22v3H2z" fill="#fff"/></svg>
    Politics<span class="chev">›</span>
  </div>
  <div class="abs topic topic--right" style="top:605px">
    <span class="chev">‹</span>Sports
    <svg width="28" height="40" viewBox="0 0 28 40"><ellipse cx="11" cy="11" rx="9" ry="10" fill="#fff"/><path d="M15 19l10 18" stroke="#fff" stroke-width="3"/></svg>
  </div>
  <div class="abs pill play">PLAY AGAIN</div>
</section>

<!-- Topic score view -->
<section class="screen screen--topic">
  <div class="abs statusbar">
    <div class="abs carrier"><span class="dots"><i class="on"></i><i class="on"></i><i></i><i></i><i></i></span>Norvia</div>
    <div class="abs time">9:32PM</div>
    <div class="abs battery"></div>
  </div>
  <div class="abs navbar">
    <svg class="abs back" width="12" height="20" viewBox="0 0 12 20"><path d="M10 2 2 10l8 8" fill="none" stroke="#ff4400" stroke-width="2"/></svg>
    <div class="abs title">You &amp; Carla</div>
    <svg class="abs share" width="24" height="34" viewBox="0 0 24 34"><path d="M8 10H1v23h22V10h-7M12 1v20M7 6l5-5 5 5" fill="none" stroke="#ff4400" stroke-width="2"/></svg>
  </div>

  <div class="abs connector" style="left:120px;top:139px;width:50px"></div>
  <div class="abs connector" style="left:250px;top:201px;width:40px"></div>
  <div class="abs avatar avatar--you" role="img" aria-label="Profile photo of You"></div>
  <div class="abs avatar avatar--carla" role="img" aria-label="Profile photo of Carla"></div>
  <div class="abs pill name--you">You</div>
  <div class="abs pill name--carla">Carla</div>

  <div class="abs band">
    <svg width="38" height="26" viewBox="0 0 28 20"><path d="M3 3h16l6 2v10l-6 2H3a2 2 0 0 1-2-2V5a2 2 0 0 1 2-2z" fill="#fff"/><circle cx="24" cy="8" r="1.5" fill="#666"/><circle cx="24" cy="12" r="1.5" fill="#666"/></svg>
    Cinema
  </div>

  <div class="abs mini-label" style="left:275px">TOTAL</div>
  <svg class="abs" style="left:265px;top:308px" width="54" height="54" viewBox="0 0 54 54"><path d="M27 4A23 23 0 1 0 44 42" fill="none" stroke="#ff4400" stroke-width="5"/></svg>
  <div class="abs mini-num" style="left:282px">58</div>
  <div class="abs mini-label" style="left:330px">IN CINEMA</div>
  <svg class="abs" style="left:329px;top:308px" width="54" height="54" viewBox="0 0 54 54"><path d="M27 4A23 23 0 0 0 8 15" fill="none" stroke="#ff4400" stroke-width="5"/></svg>
  <div class="abs mini-num" style="left:345px">15</div>

  <div class="abs panel">
    <div class="abs row lbl" style="top:22px">NUMBER OF QUESTIONS</div>
    <div class="abs row val" style="top:52px">3</div>
    <div class="abs rule"></div>
    <div class="abs row lbl" style="top:110px">TOTAL SCORE</div>
    <div class="abs row val" style="top:140px">15</div>
  </div>

  <div class="abs action action--reset">Reset Scores</div>
  <div class="abs action action--next">Go to next topic<span class="chev">›</span></div>
</section>

</div>
</body>
</html>
```